DJTarnish.net

A clean-looking fun website.

MAP*

top* Video. (To host party footage and also to host live streams as they happen.

Tabs - Events, Livestream, Mixes, Playlists, Sign up, Photos, Bio, Shop

Links to Instagram, Facebook and Twitter, YouTube & Twitch

sign up sheet to take contact details for future promo.

References
http://www.djbrindlemoss.net/
http://www.rexhollowbay.net/
https://blunkerdrave.net/
https://www.djorvanpeltsite.net/
https://nedbrisk.net/
https://www.amosvantry.net/bed/

I hope this helps.

```html
<!DOCTYPE html>
<html lang="en">
<head>
<meta charset="utf-8">
<title>DJTarnish.net</title>
<link rel="stylesheet" href="https://fonts.googleapis.com/css2?family=Montserrat:wght@400;500;600;700;800&family=Roboto:wght@400;500;700&display=swap">
<style>
:root{
  --ink:#111111;
  --white:#ffffff;
  --red:#e8131b;
  --grey:#8a8a8a;
  --light:#d9d9d9;
  --stage-purple:#4a2a6e;
  --stage-dark:#1b1b24;
  --brick:#6e2a22;
}
*{margin:0;padding:0;box-sizing:border-box}
html,body{width:1200px;height:4261px;overflow:hidden;background:var(--white);font-family:"Montserrat",sans-serif;color:var(--ink)}
.page{position:absolute;left:182px;top:116px;width:835px;height:4034px;background:var(--white);overflow:hidden}
.abs{position:absolute}
.media{position:absolute;display:block}

/* hero */
.hero{position:absolute;left:0;top:0;width:835px;height:461px;background:linear-gradient(180deg,#3b3450 0%,#5a4a63 40%,#4a3b3f 100%)}
.hero-shade{position:absolute;inset:0;background:linear-gradient(180deg,rgba(0,0,0,.35),rgba(0,0,0,.15) 50%,rgba(0,0,0,.35))}
.brand{position:absolute;left:43px;top:20px;font:800 26px "Montserrat",sans-serif;color:var(--ink);background:var(--white);padding:2px 10px;letter-spacing:.5px}
.nav{position:absolute;top:29px;left:0;width:835px;height:14px}
.nav span{position:absolute;font-size:9px;color:var(--white);transform:translateX(-50%)}
.social{position:absolute;top:28px;display:flex;gap:10px;left:713px}
.social i{display:block;width:11px;height:11px;border:1.5px solid var(--white);border-radius:3px}
.hero h1{position:absolute;top:170px;left:0;width:835px;text-align:center;color:var(--white);font:800 29px/34px "Montserrat",sans-serif;letter-spacing:.5px}
.hero p{position:absolute;top:252px;left:0;width:835px;text-align:center;color:var(--white);font-size:8px}
.btn-outline{position:absolute;left:326px;top:285px;width:100px;height:27px;border:1.5px solid var(--white);color:var(--white);font-size:7px;display:flex;align-items:center;justify-content:center}
.hero-play{position:absolute;left:439px;top:273px}

/* headings */
.section-title{position:absolute;left:0;width:835px;text-align:center;font:700 28px "Roboto",sans-serif}
.section-title::after{content:"";display:block;width:66px;height:3px;background:currentColor;margin:8px auto 0}
.body-text{font-size:7.5px;line-height:11.5px;color:#222}

/* bio */
.bio-title{left:56px;top:580px;font:700 30px "Roboto",sans-serif}
.bio-rule{left:56px;top:617px;width:85px;height:3px;background:var(--ink)}
.bio-text{left:56px;top:630px;width:290px}
.bio-text p{margin-bottom:12px}
.pill{position:absolute;background:var(--ink);color:var(--white);border-radius:14px;font:700 7px "Montserrat",sans-serif;display:flex;align-items:center;justify-content:center;letter-spacing:.3px}

/* events */
.tabs span{position:absolute;top:950px;font-size:7px;color:var(--grey);transform:translateX(-50%)}
.tabs span.active{color:var(--ink);font-weight:600}
.tab-line{left:159px;top:973px;width:525px;height:1px;background:var(--light)}
.tab-active{left:159px;top:972px;width:123px;height:2px;background:var(--ink)}
.event-arrows{position:absolute;left:368px;top:1276px;width:58px;height:28px;background:var(--ink);display:flex;justify-content:space-around;align-items:center;color:var(--white);font-size:11px}
.event-title{left:472px;top:1032px;font:600 14px "Montserrat",sans-serif}
.event-text{left:472px;top:1058px;width:305px}
.event-text p{margin-bottom:10px}
.share{left:472px;top:1230px;font-size:6px;font-weight:700}
.share-icons{left:472px;top:1246px;display:flex;gap:10px}
.share-icons i{width:9px;height:9px;border:1.3px solid var(--ink);border-radius:2px;display:block}

/* live */
.live{left:0;top:1392px;width:835px;height:474px;background:radial-gradient(ellipse at 50% 10%,#7a4b9a 0%,var(--stage-purple) 35%,#251a36 100%)}
.live .section-title{color:var(--white)}
.live-panel{left:73px;top:119px;width:705px;height:298px;background:rgba(40,40,44,.92);border-radius:6px}
.id-card{left:46px;top:22px;width:176px;height:253px;background:#121212;border-radius:6px;color:var(--white)}
.id-card h3{position:absolute;left:16px;top:50px;font:400 15px/17px "Montserrat",sans-serif}
.id-card label{position:absolute;left:16px;top:120px;font-size:9px;font-weight:600}
.id-card .field{position:absolute;left:16px;top:153px;width:112px;height:20px;background:var(--light)}
.id-card small{position:absolute;left:16px;top:185px;font-size:7px;color:#aaa}
.stream-video{left:263px;top:14px;width:401px;height:270px;background:radial-gradient(ellipse at 45% 40%,#8c8c8c 0%,#3a3a3a 25%,#0b0b0b 70%);border-radius:4px}

/* playlist */
.player{left:66px;top:2022px;width:398px;height:265px;background:linear-gradient(120deg,#2b2b2b,#6b5a52 55%,#2a2424)}
.player h4{position:absolute;left:0;width:100%;top:117px;text-align:center;color:var(--white);font:700 19px "Montserrat",sans-serif}
.progress{position:absolute;left:64px;top:214px;width:280px;height:4px;background:#aaa}
.progress b{display:block;width:120px;height:4px;background:var(--red)}
.player .t{position:absolute;top:200px;color:var(--white);font-size:7px}
.controls{position:absolute;left:66px;top:228px;color:var(--white);font-size:10px;display:flex;gap:14px}
.latest{left:522px;top:2008px;font:400 11px "Roboto",sans-serif}
.latest-rule{left:517px;top:2030px;width:212px;height:1px;background:var(--light)}
.song{position:absolute;left:517px;width:212px;height:52px;background:var(--ink);color:var(--white)}
.song .name{position:absolute;left:8px;top:14px;font-size:7px}
.song .dur{position:absolute;left:8px;top:30px;font-size:7px}
.song .thumb{position:absolute;right:0;top:0;width:75px;height:52px}
.scroll{left:759px;top:2037px;width:2px;height:250px;background:var(--ink)}
.scroll b{display:block;width:2px;height:60px;background:var(--red)}

/* mix */
.mix-art{left:66px;top:2353px;width:398px;height:315px;background:radial-gradient(ellipse at 50% 50%,#5fc3c0 0%,#8a5aa8 35%,rgba(230,120,200,.25) 65%,#ffffff 80%)}
.mix-title{left:507px;top:2381px;font:700 28px "Roboto",sans-serif}
.mix-rule{left:507px;top:2416px;width:48px;height:3px;background:var(--ink)}
.mix-text{left:507px;top:2436px;width:270px}
.mix-text p{margin-bottom:14px}

/* photos */
.photos{left:0;top:2714px;width:835px;height:509px;background:linear-gradient(180deg,#5a2a26,var(--brick) 50%,#3c1d1b)}
.photos .section-title{color:var(--white)}

/* shop */
.shirt{position:absolute;top:3405px;height:166px}
.cart{position:absolute;top:3602px;display:flex;gap:8px}
.cart i{width:25px;height:25px;background:var(--red);display:flex;align-items:center;justify-content:center}
.cart b{display:block;font-size:7px;font-weight:700;margin-top:4px}
.cart span{display:block;font-size:6px;color:var(--grey)}

/* newsletter */
.newsletter{left:0;top:3713px;width:835px;height:140px;background:var(--ink);color:var(--white)}
.newsletter .join{position:absolute;left:58px;top:36px;font:600 18px "Montserrat",sans-serif}
.newsletter .word{position:absolute;left:58px;top:62px;font:800 28px "Montserrat",sans-serif}
.email{position:absolute;left:331px;top:51px;width:336px;height:45px;background:var(--white);color:#222;font:600 14px "Montserrat",sans-serif;padding-left:16px;display:flex;align-items:center}
.submit{position:absolute;left:667px;top:51px;width:95px;height:45px;background:var(--red);color:var(--white);font:700 14px "Montserrat",sans-serif;display:flex;align-items:center;justify-content:center}

/* footer */
.foot-nav{left:0;top:3915px;width:835px;text-align:center;font:400 15px "Roboto",sans-serif;word-spacing:2px}
.foot-nav span{margin:0 6px}
.foot-rule{left:149px;top:3954px;width:535px;height:1px;background:#cfcfcf}
.copy{left:0;top:3968px;width:835px;text-align:center;font-size:6px;color:#555}
.foot-icons{left:0;top:3990px;width:835px;display:flex;justify-content:center;gap:14px}
.foot-icons i{width:8px;height:8px;background:var(--ink);border-radius:50%;display:block}
</style>
</head>
<body>
<main class="page">

  <header class="hero">
    <div class="media" role="img" aria-label="Photo of a smiling DJ with headphones among a cheering crowd" style="inset:0;background:linear-gradient(120deg,#2f2a44,#6e5866 45%,#8a7a80 60%,#3e3440)"></div>
    <div class="hero-shade"></div>
    <div class="brand">DJTarnish</div>
    <nav class="nav">
      <span style="left:234px">Events</span><span style="left:293px">Livestream</span><span style="left:353px">Mixes</span><span style="left:406px">Playlists</span><span style="left:464px">Sign up</span><span style="left:517px">Photos</span><span style="left:562px">Bio</span><span style="left:605px">Shop</span>
    </nav>
    <div class="social"><i></i><i></i><i></i><i></i></div>
    <h1>DJ AND LIVE<br>STREAM ENTERTAINMENT</h1>
    <p>Lorem ipsum dolor sit amet, consectetur adipiscing elit.</p>
    <div class="btn-outline">Enter to the Stream</div>
    <svg class="hero-play" width="52" height="52" viewBox="0 0 52 52"><circle cx="26" cy="26" r="24" fill="none" stroke="#fff" stroke-width="2.5"/><path d="M20 15 L38 26 L20 37 Z" fill="#fff"/></svg>
  </header>

  <h2 class="abs bio-title">Biography</h2>
  <div class="abs bio-rule"></div>
  <div class="abs bio-text body-text">
    <p>Lorem ipsum dolor sit amet, consectetur adipiscing elit. Molestie scelerisque volutpat consectetur laoreet purus fermentum commodo, nullam vulputate. Praesent lorem elementum ac aliquet. Arcu vulputate urna bibendum elementum cursus suscipit nunc faucibus posuere. Convallis neque amet fermentum sed. Porttitor nibh amet pretium suscipit dapibus consequat tincidunt. Sit nunc, felis cursus adipiscing posuere vulputate.</p>
    <p>Auctor mauris orci fusce tortor, velit, non tellus. Risus, nisl aliquet aenean et maecenas sed urna nulla. Imperdiet habitant convallis sit augue.</p>
    <p>Auctor mauris orci fusce tortor, velit, non tellus. Risus, nisl aliquet aenean et maecenas sed urna nulla. Imperdiet habitant convallis sit augue.</p>
  </div>
  <div class="pill" style="left:60px;top:790px;width:91px;height:27px">READ MORE</div>
  <div class="media" role="img" aria-label="Photo of a DJ singing into a microphone behind decks in warm orange light" style="left:418px;top:565px;width:362px;height:240px;background:radial-gradient(ellipse at 60% 35%,#e9a055 0%,#a34f1c 40%,#2a140a 100%)"></div>

  <h2 class="section-title" style="top:852px">Events</h2>
  <div class="tabs">
    <span class="active" style="left:224px">Night Parties</span><span style="left:353px">Beach Parties</span><span style="left:486px">Farmhouse Parties</span><span style="left:620px">Road Parties</span>
  </div>
  <div class="abs tab-line"></div>
  <div class="abs tab-active"></div>
  <div class="media" role="img" aria-label="Photo of a DJ with headphones under red and blue club lights" style="left:50px;top:1031px;width:376px;height:273px;background:linear-gradient(130deg,#d42a2a,#7a1030 40%,#2a2a8a 75%,#c43a20)"></div>
  <div class="event-arrows"><span>&#8592;</span><span>&#8594;</span></div>
  <h3 class="abs event-title">Night party</h3>
  <div class="abs event-text body-text">
    <p>Lorem ipsum dolor sit amet, consectetur adipiscing elit. Viverra eu cursus et tellus suscipit. A fames urna, mattis diam. Aliquam placerat lacus augue leo interdum id amet fringilla. Tempor sem purus pellentesque proin semper. Eget morbi odio donec pellentesque. Id vitae sit cras id sit. Nunc, quis dictumst non tellus posuere. Viverra eu cursus et tellus suscipit.</p>
    <p>Lorem ipsum dolor sit amet, consectetur adipiscing elit. Viverra eu cursus et tellus suscipit. A fames urna, mattis diam. Aliquam placerat lacus augue leo interdum id amet fringilla. Tempor sem purus pellentesque proin semper. Eget morbi odio donec pellentesque. Id vitae sit cras id sit. Nunc, quis dictumst non tellus posuere.</p>
  </div>
  <div class="abs share">SHARE IT:</div>
  <div class="abs share-icons"><i></i><i></i><i></i></div>
  <div class="pill" style="left:469px;top:1278px;width:122px;height:27px">SEE OUR LAST EVENT</div>

  <section class="abs live">
    <div class="media" role="img" aria-label="Photo of a concert crowd under purple stage lights" style="inset:0;background:radial-gradient(ellipse at 50% 0%,#8d5bb0 0%,#4a2a6e 40%,#1e1428 100%)"></div>
    <h2 class="section-title" style="top:42px">Live Stream</h2>
    <div class="abs live-panel">
      <div class="abs id-card">
        <h3>write your<br>id to enter<br>the stream</h3>
        <label>Enter ID</label>
        <div class="field"></div>
        <small>JOIN</small>
      </div>
      <div class="media stream-video" role="img" aria-label="Video still of a crowd facing a brightly lit stage"></div>
      <svg class="abs" style="left:478px;top:104px" width="92" height="92" viewBox="0 0 92 92"><circle cx="46" cy="46" r="42" fill="none" stroke="#fff" stroke-width="4"/><path d="M36 28 L64 46 L36 64 Z" fill="#fff"/></svg>
    </div>
  </section>

  <h2 class="section-title" style="top:1928px">Playlist</h2>
  <div class="media player" role="img" aria-label="Photo of a singer at a microphone">
    <h4>It's Not Easy</h4>
    <span class="t" style="left:64px">2:38</span><span class="t" style="left:320px">6:05</span>
    <div class="progress"><b></b></div>
    <div class="controls"><span>&#9664;&#9664;</span><span>&#9654;</span><span>&#9654;&#9654;</span></div>
  </div>
  <div class="abs latest">Latest Songs</div>
  <div class="abs latest-rule"></div>
  <div class="song" style="top:2046px"><span class="name">Lorem ipsum dolor</span><span class="dur">&#9654;&nbsp; 5:05</span><div class="media thumb" role="img" aria-label="Photo of a performer in pink light" style="background:linear-gradient(135deg,#2a1030,#c2306a)"></div></div>
  <div class="song" style="top:2111px"><span class="name">Lorem ipsum dolor</span><span class="dur">&#9654;&nbsp; 3:25</span><div class="media thumb" role="img" aria-label="Photo of a performer in blue light" style="background:linear-gradient(135deg,#101a4a,#5a3aa8)"></div></div>
  <div class="song" style="top:2172px"><span class="name">Lorem ipsum dolor</span><span class="dur">&#9654;&nbsp; 4:58</span><div class="media thumb" role="img" aria-label="Photo of a performer on stage" style="background:linear-gradient(135deg,#3a2a5a,#b04a8a)"></div></div>
  <div class="song" style="top:2234px"><span class="name">Lorem ipsum dolor</span><span class="dur">&#9654;&nbsp; 3:55</span><div class="media thumb" role="img" aria-label="Photo of a singer with a microphone" style="background:linear-gradient(135deg,#1a1a3a,#4a5ab0)"></div></div>
  <div class="abs scroll"><b></b></div>

  <div class="media mix-art" role="img" aria-label="Illustration of colourful cassette tapes over a sound wave"></div>
  <h2 class="abs mix-title">Mix</h2>
  <div class="abs mix-rule"></div>
  <div class="abs mix-text body-text">
    <p>Lorem ipsum dolor sit amet, consectetur adipiscing elit. Viverra eu cursus et tellus suscipit. A fames urna, mattis diam. Aliquam placerat lacus augue leo interdum id amet fringilla. Tempor sem purus pellentesque proin semper. Eget morbi odio donec pellentesque. Id vitae sit cras id sit. Nunc, quis dictumst non tellus posuere.</p>
    <p>Lorem ipsum dolor sit amet, consectetur adipiscing elit. Viverra eu cursus et tellus suscipit. A fames urna, mattis diam. Aliquam placerat lacus augue leo interdum id amet fringilla. Tempor sem purus pellentesque proin semper. Eget morbi odio donec pellentesque. Id vitae sit cras id sit.</p>
  </div>

  <section class="abs photos">
    <div class="media" role="img" aria-label="Background photo of a brick wall and DJ equipment" style="inset:0;background:linear-gradient(180deg,#5e2a25,#7a3026 55%,#3a1c1a)"></div>
    <h2 class="section-title" style="top:40px">Photos</h2>
    <div class="media" role="img" aria-label="Photo of a DJ in a white shirt under yellow lights" style="left:43px;top:121px;width:244px;height:277px;background:linear-gradient(160deg,#e8d24a,#8a7a2a 45%,#2a2218)"></div>
    <div class="media" role="img" aria-label="Photo of hands on a turntable in purple light" style="left:297px;top:121px;width:235px;height:128px;background:linear-gradient(135deg,#1a1040,#6a3ab0 60%,#2a1a50)"></div>
    <div class="media" role="img" aria-label="Photo of a DJ controller seen from above" style="left:297px;top:256px;width:235px;height:142px;background:linear-gradient(135deg,#cfd4da,#3a3f48 55%,#1a1d22)"></div>
    <div class="media" role="img" aria-label="Photo of a DJ with headphones in red club light" style="left:558px;top:121px;width:244px;height:277px;background:linear-gradient(160deg,#3a3a6a,#b0283a 50%,#2a1018)"></div>
  </section>

  <h2 class="section-title" style="top:3300px">Our shop</h2>
  <div class="media shirt" role="img" aria-label="White T-shirt with printed headphones graphic" style="left:33px;width:133px;background:radial-gradient(ellipse at 50% 50%,#f4f4f4 40%,#fff 72%)"></div>
  <div class="media shirt" role="img" aria-label="Black T-shirt with colourful print" style="left:235px;width:133px;background:radial-gradient(ellipse at 50% 50%,#1d1d1d 42%,#fff 70%)"></div>
  <div class="media shirt" role="img" aria-label="Grey T-shirt with music slogan print" style="left:456px;width:124px;background:radial-gradient(ellipse at 50% 50%,#9a9a9a 42%,#fff 70%)"></div>
  <div class="media shirt" role="img" aria-label="White ringer T-shirt with record print" style="left:650px;width:126px;background:radial-gradient(ellipse at 50% 50%,#efefef 42%,#fff 70%)"></div>
  <div class="cart" style="left:33px"><i><svg width="14" height="12" viewBox="0 0 14 12"><path d="M1 1h2l2 7h7l1.5-5H4" fill="none" stroke="#fff" stroke-width="1.5"/><circle cx="6" cy="10.5" r="1.2" fill="#fff"/><circle cx="11" cy="10.5" r="1.2" fill="#fff"/></svg></i><div><b>Add to card</b><span>15.0$</span></div></div>
  <div class="cart" style="left:246px"><i><svg width="14" height="12" viewBox="0 0 14 12"><path d="M1 1h2l2 7h7l1.5-5H4" fill="none" stroke="#fff" stroke-width="1.5"/><circle cx="6" cy="10.5" r="1.2" fill="#fff"/><circle cx="11" cy="10.5" r="1.2" fill="#fff"/></svg></i><div><b>Add to card</b><span>15.0$</span></div></div>
  <div class="cart" style="left:461px"><i><svg width="14" height="12" viewBox="0 0 14 12"><path d="M1 1h2l2 7h7l1.5-5H4" fill="none" stroke="#fff" stroke-width="1.5"/><circle cx="6" cy="10.5" r="1.2" fill="#fff"/><circle cx="11" cy="10.5" r="1.2" fill="#fff"/></svg></i><div><b>Add to card</b><span>15.0$</span></div></div>
  <div class="cart" style="left:667px"><i><svg width="14" height="12" viewBox="0 0 14 12"><path d="M1 1h2l2 7h7l1.5-5H4" fill="none" stroke="#fff" stroke-width="1.5"/><circle cx="6" cy="10.5" r="1.2" fill="#fff"/><circle cx="11" cy="10.5" r="1.2" fill="#fff"/></svg></i><div><b>Add to card</b><span>15.0$</span></div></div>

  <section class="abs newsletter">
    <div class="join">Join our</div>
    <div class="word">Newsletter</div>
    <div class="email">Enter you email</div>
    <div class="submit">SUBMIT</div>
  </section>

  <nav class="abs foot-nav"><span>Events</span><span>Livestream</span><span>Mixes</span><span>Playlists</span><span>Sign up</span><span>Photos</span><span>Bio</span><span>Shop</span></nav>
  <div class="abs foot-rule"></div>
  <div class="abs copy">Copyright 2021 Tarnish | All Right Reserver</div>
  <div class="abs foot-icons"><i></i><i></i><i></i><i></i></div>

</main>
</body>
</html>
```